Business Card Design Project

Business card for new event planning company. I will load in 2 different colors of logs for you to use.

Target Market(s)

meeting planners and business leaders

Industry/Entity Type

Event Planning

Requirements
Must have
• memorable/ creative please - maybe logo on back of the card

Information for business card: (Information may change)

LaVonna Birchwell
lav@MarigoldOccasionsandGatherings.com
www.MarigoldOccasionsandGatherings.com
555.730.2964
Nice to have
• Do you think it would be too much to add twiiter, FB, linked in logo to card to connect?

all are LaVonna Birchwell

```html
<!DOCTYPE html>
<html lang="en">
<head>
<meta charset="utf-8">
<title>Marigold Occasions &amp; Gatherings — Business Card</title>
<link rel="stylesheet" href="https://fonts.googleapis.com/css2?family=Oswald:wght@500;600&family=Roboto+Condensed:wght@400;500&display=swap">
<style>
  :root {
    --stage: #d6d6d8;
    --card-cream: #f0eee0;
    --card-dark: #2b2a2f;
    --ink: #1f1f22;
    --purple: #8b79d9;
    --purple-soft: #b1a6e8;
    --dot: #1f1f22;
  }
  * { box-sizing: border-box; margin: 0; padding: 0; }
  html, body {
    width: 1200px; height: 900px; overflow: hidden;
    background: var(--stage);
  }
  .stage {
    position: relative; width: 1200px; height: 900px;
  }

  /* Front of card (vertical) */
  .card-front {
    position: absolute; left: 110px; top: 140px;
    width: 360px; height: 630px;
    background: var(--card-cream);
    box-shadow: 0 6px 18px rgba(0,0,0,.18);
    padding: 48px 34px 40px 40px;
    display: flex; flex-direction: column;
  }
  .front-brand {
    display: flex; align-items: center; gap: 12px;
    height: 120px;
  }
  .brand-dot {
    width: 26px; height: 26px; border-radius: 50%;
    background: var(--purple); flex: none;
  }
  .front-brand .brand-name {
    font-family: "Roboto Condensed", sans-serif;
    font-weight: 500; font-size: 26px; color: var(--purple);
    letter-spacing: .5px;
  }
  .person-name {
    margin-top: 46px;
    font-family: "Oswald", sans-serif; font-weight: 600;
    font-size: 50px; line-height: 1.02; letter-spacing: 1px;
    text-transform: uppercase; color: var(--ink);
  }
  .contact-list { margin-top: 34px; list-style: none; }
  .contact-rule {
    height: 4px; margin: 16px 0;
    background-image: radial-gradient(circle, var(--dot) 1.8px, transparent 2px);
    background-size: 11px 4px; background-repeat: repeat-x;
  }
  .contact-item {
    font-family: "Roboto Condensed", sans-serif; font-size: 17px;
    color: var(--ink); white-space: nowrap;
  }
  .contact-phone { text-align: right; font-size: 19px; }
  .contact-web { color: var(--purple); font-size: 17px; font-weight: 500; }

  /* Back of card (horizontal) */
  .card-back {
    position: absolute; left: 540px; top: 200px;
    width: 570px; height: 325px;
    background: linear-gradient(160deg, #36353b 0%, var(--card-dark) 60%, #232227 100%);
    box-shadow: 0 6px 18px rgba(0,0,0,.25);
    display: flex; align-items: center; justify-content: center;
  }
  .back-brand {
    display: flex; align-items: center; gap: 16px;
  }
  .back-brand .brand-name {
    font-family: "Roboto Condensed", sans-serif;
    font-weight: 500; font-size: 34px; color: var(--purple-soft);
    letter-spacing: .5px;
  }
  .back-brand .brand-dot { width: 30px; height: 30px; background: var(--purple-soft); }
</style>
</head>
<body>
<main class="stage">
  <section class="card-front" aria-label="Card front">
    <div class="front-brand">
      <span class="brand-dot"></span>
      <span class="brand-name">Marigold</span>
    </div>
    <h1 class="person-name">LaVonna<br>Birchwell</h1>
    <ul class="contact-list">
      <li class="contact-rule" aria-hidden="true"></li>
      <li class="contact-item contact-phone">T: 555.730.2964</li>
      <li class="contact-rule" aria-hidden="true"></li>
      <li class="contact-item contact-email">lav@MarigoldOccasionsandGatherings.com</li>
      <li class="contact-rule" aria-hidden="true"></li>
      <li class="contact-item contact-web">www.MarigoldOccasionsandGatherings.com</li>
    </ul>
  </section>

  <section class="card-back" aria-label="Card back">
    <div class="back-brand">
      <span class="brand-name">Marigold Occasions &amp; Gatherings</span>
      <span class="brand-dot"></span>
    </div>
  </section>
</main>
</body>
</html>
```